HOME IMPROVEMENT Business Card

I want a very unique business card. nothing typical and boring. Im open to you ideas. Ive seen cards with gold and silver or color foil and spot UV coatings. Im looking for something that looks cool and grabs attention. I like rounded corners but am open to all suggestions. We are a home improvement company and I will have a presentation folder printed and a catalog printed also and want to keep that same theme. I love the colors in our logo but I am open at looking at a 3rd color that would work with my logo. I hope that helps.
Card should include
Address
Phone
Fax
Email
Website
Target Market(s)
Home owners, people looking to remodel their home
Industry/Entity Type
Home Improvement
Contact Information for Business Card
2873 Maple Crest Avenue Unit 410
Des Plaines, Il 60284
Phone
Direct Line
Email
Website
Font styles to use
Other font styles liked:
- IM OPEN MINDED
Requirements
Must have
- High end quality look nothing boring I like rounded corners but am open minded
Nice to have
- WOW. I want something nice and impressive.
Should not have
- ??? Not sure

```html
<!DOCTYPE html>
<html lang="en">
<head>
<meta charset="utf-8">
<title>NestCraft Business Card</title>
<link href="https://fonts.googleapis.com/css2?family=Arimo:wght@400;700&display=swap" rel="stylesheet">
<style>
  :root {
    --green: #0a9a48;
    --green-light: #2fc06c;
    --navy: #141a45;
    --foil: #c9a54c;
    --foil-light: #f1dc9a;
    --paper: #f5f5f5;
    --paper-shade: #ebebeb;
    --ink: #1c1c1c;
    --backdrop: #e9e9e9;
  }
  * { box-sizing: border-box; margin: 0; padding: 0; }
  html, body {
    width: 1200px; height: 586px; overflow: hidden;
    background: var(--backdrop);
    font-family: "Arimo", Arial, sans-serif;
  }
  .canvas { position: relative; width: 1200px; height: 586px; }
  .card {
    position: absolute; top: 129px; width: 501px; height: 301px;
    background: linear-gradient(135deg, var(--paper) 0%, #fafafa 45%, var(--paper-shade) 100%);
    border-radius: 14px; overflow: hidden;
  }
  .card--front { left: 61px; }
  .card--back { left: 619px; }

  .band { position: absolute; left: 0; right: 0; }
  .band--green { height: 12px; background: linear-gradient(90deg, var(--green) 0%, var(--green-light) 50%, var(--green) 100%); }
  .band--foil { height: 2px; background: linear-gradient(90deg, var(--foil) 0%, var(--foil-light) 50%, var(--foil) 100%); }
  .band--navy { height: 5px; background: var(--navy); }
  .card--front .band--green { top: 0; }
  .card--front .band--foil { top: 12px; }
  .card--front .band--navy { top: 14px; }
  .card--back .band--navy { bottom: 14px; }
  .card--back .band--foil { bottom: 12px; }
  .card--back .band--green { bottom: 0; }

  .brand { display: flex; align-items: center; gap: 10px; color: var(--navy); font-weight: 700; }
  .brand__dot { background: var(--green); border-radius: 50%; }
  .brand--large {
    position: absolute; left: 0; right: 0; top: 140px; justify-content: center;
    font-size: 58px; letter-spacing: -1px; line-height: 66px;
  }
  .brand--large .brand__dot { width: 30px; height: 30px; }
  .brand--small { position: absolute; left: 28px; top: 62px; font-size: 30px; gap: 7px; line-height: 36px; }
  .brand--small .brand__dot { width: 16px; height: 16px; }

  .person { position: absolute; right: 30px; top: 156px; text-align: right; }
  .person__name { color: var(--green); font-weight: 700; font-size: 17px; line-height: 20px; }
  .person__role { color: var(--ink); font-size: 10.5px; line-height: 12px; margin-top: 6px; }
  .rule { position: absolute; left: 28px; width: 365px; top: 182px; height: 2px; background: var(--ink); }

  .contacts { position: absolute; left: 28px; top: 196px; list-style: none; }
  .contacts li { display: flex; align-items: center; gap: 8px; height: 20px; font-size: 11.5px; color: var(--ink); white-space: nowrap; }
  .contacts li.contacts__mail, .contacts li.contacts__web { font-size: 10.5px; }
  .contacts svg { width: 16px; height: 16px; flex: none; }

  .address {
    position: absolute; right: 30px; top: 226px; text-align: right;
    color: var(--green); font-weight: 700; font-size: 12.5px; line-height: 17px; font-style: normal;
  }
</style>
</head>
<body>
<div class="canvas">
  <section class="card card--front">
    <div class="band band--green"></div>
    <div class="band band--foil"></div>
    <div class="band band--navy"></div>
    <div class="brand brand--large"><span class="brand__dot"></span>NestCraft</div>
  </section>

  <section class="card card--back">
    <div class="brand brand--small"><span class="brand__dot"></span>NestCraft</div>

    <div class="person">
      <p class="person__name">Marcus Hale</p>
      <p class="person__role">Sales Director</p>
    </div>
    <div class="rule"></div>

    <ul class="contacts">
      <li>
        <svg viewBox="0 0 18 18" aria-hidden="true"><circle cx="9" cy="9" r="9" fill="var(--green)"/><path d="M5 8.5c0-2 8-2 8 0v1h-2v-1.2H7v1.2H5z M6.5 10h5l1 3h-7z" fill="#fff"/></svg>
        +33 6 41 82 19 07
      </li>
      <li>
        <svg viewBox="0 0 18 18" aria-hidden="true"><circle cx="9" cy="9" r="9" fill="var(--green)"/><rect x="6.5" y="4.5" width="5" height="3" fill="#fff"/><rect x="4.5" y="7.5" width="9" height="4" rx="1" fill="#fff"/><rect x="6.5" y="10.5" width="5" height="3" fill="#fff" stroke="var(--green)" stroke-width=".6"/></svg>
        +33 9 58 30 44 26
      </li>
      <li class="contacts__mail">
        <svg viewBox="0 0 18 18" aria-hidden="true"><circle cx="9" cy="9" r="9" fill="var(--green)"/><rect x="4.5" y="5.5" width="9" height="7" fill="#fff"/><path d="M4.5 5.5L9 9.5l4.5-4" fill="none" stroke="var(--green)" stroke-width="1"/></svg>
        m.hale@nestcraftgroup.fr
      </li>
      <li class="contacts__web">
        <svg viewBox="0 0 18 18" aria-hidden="true"><circle cx="9" cy="9" r="9" fill="var(--green)"/><circle cx="9" cy="9" r="4.5" fill="none" stroke="#fff" stroke-width="1"/><ellipse cx="9" cy="9" rx="2" ry="4.5" fill="none" stroke="#fff" stroke-width="1"/><path d="M4.5 9h9" stroke="#fff" stroke-width="1"/></svg>
        www.nestcraftgroup.fr
      </li>
    </ul>

    <address class="address">18 rue Verlaine,<br>75011 Paris, France</address>

    <div class="band band--navy"></div>
    <div class="band band--foil"></div>
    <div class="band band--green"></div>
  </section>
</div>
</body>
</html>
```